Need Business cards

Im a new realtor and already have a logo. I would like to purchase a Business card design that catches customer's attention, its creative, and modern.

Marisol Quintero
Realtor ®
(555) 318 4027
marisolqtrhomes@brindlemail.com

Target Market(s)

investors, buyers and seller, property management

Industry/Entity Type

real estate,

Contact Information for Business Card

Marisol Quintero

Requirements
Must have
• BOTH LOGOS, WOULD LIKE TO SEE WITH DIFFERENT OPTIONS WITH EITHER PICTURE

```html
<!DOCTYPE html>
<html lang="en">
<head>
<meta charset="UTF-8">
<title>Marisol Quintero — Realtor Business Cards</title>
<link href="https://fonts.googleapis.com/css2?family=Poppins:wght@400;500;600;700&display=swap" rel="stylesheet">
<style>
  :root {
    --stage: #ece8e1;
    --card-white: #ffffff;
    --cream: #f4ecdc;
    --cream-deep: #e6d7b8;
    --gold: #c59a2e;
    --gold-light: #e2c16a;
    --navy: #1f2b4d;
    --broker-blue: #2f62c4;
    --shadow: rgba(60, 45, 20, 0.18);
  }
  * { box-sizing: border-box; margin: 0; padding: 0; }
  html, body {
    width: 1200px; height: 800px; overflow: hidden;
    background: var(--stage);
    font-family: "Poppins", sans-serif;
  }
  .stage {
    position: relative; width: 1200px; height: 800px;
    display: flex; align-items: center; justify-content: center; gap: 40px;
  }
  .card {
    position: relative; width: 540px; height: 309px;
    background: var(--card-white);
    box-shadow: 0 12px 30px var(--shadow);
    overflow: hidden;
  }

  /* Back card */
  .card-back .pattern-field {
    position: absolute; inset: 0;
    background: radial-gradient(ellipse at 40% 40%, #ffffff 0%, #f6f0e4 55%, #ece1cb 100%);
  }
  .card-back .brand-mark {
    position: absolute; left: 50%; top: 50%;
    transform: translate(-50%, -50%);
    display: flex; align-items: center; gap: 12px;
  }
  .brand-square {
    width: 14px; height: 14px; background: var(--gold);
  }
  .brand-name {
    font-weight: 600; color: var(--gold);
    letter-spacing: 2px; text-transform: uppercase;
  }
  .card-back .brand-name { font-size: 24px; }

  /* Front card */
  .card-front .sweep { position: absolute; inset: 0; }
  .card-front .brand-mark {
    position: absolute; left: 70px; top: 92px;
    display: flex; align-items: center; gap: 10px;
  }
  .card-front .brand-name { font-size: 18px; }
  .agent-title {
    position: absolute; right: 24px; top: 58px; text-align: right;
  }
  .agent-name {
    font-size: 17px; font-weight: 700; color: var(--navy); letter-spacing: 0.5px;
    text-transform: uppercase;
  }
  .agent-role {
    font-size: 11px; font-weight: 500; color: var(--navy); margin-top: 2px;
  }
  .contact-list {
    position: absolute; left: 44px; top: 176px; list-style: none;
  }
  .contact-item {
    display: flex; align-items: center; gap: 10px;
    font-size: 16px; font-weight: 500; color: var(--navy); margin-bottom: 8px;
  }
  .contact-item svg { width: 16px; height: 16px; flex: none; }
  .contact-email { font-size: 14px; }
  .broker-name {
    position: absolute; left: 44px; bottom: 26px;
    font-size: 18px; font-weight: 700; color: var(--broker-blue);
    letter-spacing: 1px; text-transform: uppercase;
  }
  .agent-portrait {
    position: absolute; right: 40px; bottom: 0; width: 150px; height: 200px;
    background: linear-gradient(180deg, #d9c3a0 0%, #e7cf8f 45%, #f3ecdf 100%);
    border-radius: 70px 70px 0 0;
  }
</style>
</head>
<body>
<main class="stage">

  <section class="card card-back" aria-label="Business card back">
    <div class="pattern-field" role="img" aria-label="Soft cream decorative leaf pattern"></div>
    <div class="brand-mark">
      <span class="brand-square"></span>
      <span class="brand-name">Marisol Quintero</span>
    </div>
  </section>

  <section class="card card-front" aria-label="Business card front">
    <svg class="sweep" viewBox="0 0 540 309" preserveAspectRatio="none" aria-hidden="true">
      <defs>
        <linearGradient id="sweepGold" x1="0" y1="0" x2="1" y2="1">
          <stop offset="0" stop-color="#f7f1e4"/>
          <stop offset="1" stop-color="#e9dcc0"/>
        </linearGradient>
      </defs>
      <rect width="540" height="309" fill="#fdfbf7"/>
      <path d="M250 0 C 300 110, 300 220, 220 309 L540 309 L540 0 Z" fill="url(#sweepGold)"/>
      <path d="M330 0 C 380 120, 400 230, 380 309 L540 309 L540 0 Z" fill="#fbf7ef" opacity="0.8"/>
    </svg>

    <div class="brand-mark">
      <span class="brand-square"></span>
      <span class="brand-name">Marisol Quintero</span>
    </div>

    <div class="agent-title">
      <p class="agent-name">Marisol Quintero</p>
      <p class="agent-role">Realtor ®</p>
    </div>

    <ul class="contact-list">
      <li class="contact-item">
        <svg viewBox="0 0 24 24"><path fill="var(--gold)" d="M6.6 10.8a15.1 15.1 0 0 0 6.6 6.6l2.2-2.2a1 1 0 0 1 1-.25 11.4 11.4 0 0 0 3.6.57 1 1 0 0 1 1 1V20a1 1 0 0 1-1 1A17 17 0 0 1 3 4a1 1 0 0 1 1-1h3.5a1 1 0 0 1 1 1c0 1.25.2 2.45.57 3.6a1 1 0 0 1-.25 1z"/></svg>
        <span>(555) 318 4027</span>
      </li>
      <li class="contact-item contact-email">
        <svg viewBox="0 0 24 24"><rect x="2" y="5" width="20" height="14" rx="1.5" fill="var(--gold)"/><path d="M3 6l9 7 9-7" fill="none" stroke="#fff" stroke-width="1.6"/></svg>
        <span>marisolqtrhomes@brindlemail.com</span>
      </li>
    </ul>

    <p class="broker-name">Crestline Realty</p>

    <div class="agent-portrait" role="img" aria-label="Portrait photo of the realtor in a cream blazer"></div>
  </section>

</main>
</body>
</html>
```